Need someone to design a book cover for a book called A Copper Lantern. The layout needs to be on a 5"x 8" with a 0.75" spine and a 1/8" bleed.

I would like the background of the cover to include the columns from the temple of Verdant Marlo in Athens (stiles verdantou marlo).

The book is a psychological sexual thriller taking place in modern Athens during a financial crisis.

Please leave a text placeholder on the back of the cover.

```html
<!DOCTYPE html>
<html lang="en">
<head>
<meta charset="utf-8">
<title>A Copper Lantern – Book Cover Wrap</title>
<link href="https://fonts.googleapis.com/css2?family=Anton&family=Open+Sans:wght@700&family=Questrial&display=swap" rel="stylesheet">
<style>
  :root {
    --yellow: #ffe600;
    --yellow-warm: #ffd000;
    --orange: #ffae00;
    --ink: #0d0a00;
    --title-yellow: #ffe600;
  }
  html, body {
    margin: 0;
    padding: 0;
    width: 1200px;
    height: 898px;
    overflow: hidden;
    background: var(--orange);
  }
  .cover {
    position: relative;
    width: 1200px;
    height: 898px;
    overflow: hidden;
    background:
      radial-gradient(ellipse 70% 60% at 22% 45%, var(--yellow) 0%, var(--yellow-warm) 60%, var(--orange) 100%),
      var(--yellow);
  }
  .cover__front-glow {
    position: absolute;
    left: 642px; top: 0;
    width: 558px; height: 898px;
    background: radial-gradient(ellipse 75% 65% at 50% 40%, var(--yellow) 0%, var(--yellow-warm) 60%, var(--orange) 100%);
  }
  .spine {
    position: absolute;
    left: 558px; top: 0;
    width: 84px; height: 898px;
    background: linear-gradient(90deg, var(--orange) 0%, var(--yellow) 35%, var(--yellow) 65%, var(--yellow-warm) 100%);
  }
  .spine__title {
    position: absolute;
    left: 21px; top: 103px;
    width: 49px; height: 349px;
    background: var(--ink);
    color: var(--title-yellow);
    writing-mode: vertical-rl;
    font-family: "Anton", sans-serif;
    font-size: 37px;
    line-height: 49px;
    text-align: center;
    letter-spacing: 1px;
    text-transform: uppercase;
    white-space: nowrap;
  }
  .spine__author {
    position: absolute;
    left: 22px; top: 568px;
    width: 40px; height: 212px;
    writing-mode: vertical-rl;
    font-family: "Questrial", sans-serif;
    font-size: 25px;
    line-height: 40px;
    letter-spacing: 1.5px;
    color: var(--ink);
    white-space: nowrap;
  }
  .back__blurb {
    position: absolute;
    left: 69px; top: 176px;
    width: 443px;
    margin: 0;
    font-family: "Open Sans", sans-serif;
    font-weight: 700;
    font-size: 15.3px;
    line-height: 28px;
    color: var(--ink);
    text-align: justify;
    hyphens: auto;
  }
  .front__column {
    position: absolute;
    top: 123px;
    width: 109px;
    height: 648px;
    background: var(--ink);
  }
  .front__column--left { left: 748px; }
  .front__column--right { left: 972px; }
  .front__title-line {
    position: absolute;
    background: var(--ink);
    color: var(--title-yellow);
    font-family: "Anton", sans-serif;
    text-transform: uppercase;
    text-align: center;
    white-space: nowrap;
  }
  .front__title-line--top {
    left: 665px; top: 257px;
    width: 489px; height: 97px;
    font-size: 86px;
    line-height: 97px;
    letter-spacing: 2px;
  }
  .front__title-line--main {
    left: 672px; top: 365px;
    width: 484px; height: 196px;
    font-size: 150px;
    line-height: 196px;
    letter-spacing: 1px;
  }
  .front__author {
    position: absolute;
    left: 648px; top: 815px;
    width: 540px;
    text-align: center;
    font-family: "Questrial", sans-serif;
    font-size: 40px;
    letter-spacing: 3px;
    color: var(--ink);
    word-spacing: 10px;
  }
</style>
</head>
<body>
<main class="cover">
  <section class="back">
    <p class="back__blurb">Lorem ipsum dolor sit amet, consectetur adipiscing elit, sed do eiusmod tempor incididunt ut labore et dolore magna aliqua. Quis ipsum suspendisse ultrices gravida. Risus commodo viverra maecenas accumsan lacus vel facilisis. Lorem ipsum dolor sit amet, consectetur adipiscing elit, sed do eiusmod tempor incididunt ut labore et dolore magna aliqua. Quis ipsum suspendisse ultrices gravida. Risus commodo viverra maecenas accumsan lacus vel facilisis. Lorem ipsum dolor sit amet, consectetur adipiscing elit, sed do eiusmod tempor incididunt ut labore et dolore magna aliqua. Quis ipsum suspendisse ultrices gravida. Risus commodo viverra maecenas accumsan lacus vel facilisis. Lorem ipsum dolor sit amet, consectetur adipiscing elit, sed do eiusmod tempor incididunt ut labore et dolore magna aliqua. Quis ipsum suspendisse ultrices gravida. Risus commodo viverra maecenas accumsan lacus vel facilisis.</p>
  </section>

  <section class="spine">
    <div class="spine__title">A Copper Lantern</div>
    <div class="spine__author">AUTHOR NAME</div>
  </section>

  <section class="front">
    <div class="cover__front-glow"></div>
    <div class="front__column front__column--left" role="img" aria-label="Black silhouette of a Corinthian column from the temple of Verdant Marlo"></div>
    <div class="front__column front__column--right" role="img" aria-label="Black silhouette of a Corinthian column from the temple of Verdant Marlo"></div>
    <h1 class="front__title">
      <span class="front__title-line front__title-line--top">A Copper</span>
      <span class="front__title-line front__title-line--main">Lantern</span>
    </h1>
    <div class="front__author">AUTHOR NAME</div>
  </section>
</main>
</body>
</html>
```